Halvery Building Group Website

Need a dynamic corporate website that can be built on with time. We want to get our information out to the world and have a place where customers can submit requests for proposals.

Target Market(s)

Custom home owners and buyers. Architects and Real Estate Agents.

Industry/Entity Type

Construction

Number of Pages Required

3 page

Font styles to use
Serif
Sans Serif

Requirements
Must have
• Company logo, about, company contact information, biography, contact, projects,
• Sleek, modern, clean, attractive design.
• Online form customers can use for filling out a request for project proposal.
• Workcircle hyperlink.
• Uses www.halverybuildinggroup.example

```html
<!DOCTYPE html>
<html lang="en">
<head>
<meta charset="utf-8">
<title>Halvery Building Group</title>
<link rel="stylesheet" href="https://fonts.googleapis.com/css2?family=Josefin+Sans:wght@300;400;600&family=Open+Sans:wght@400;600;700&family=Raleway:wght@300;400;600&display=swap">
<style>
:root{
  --blue:#1f63b3;
  --blue-dark:#0f2f55;
  --ink:#2b2b2b;
  --muted:#7a7a7a;
  --line:#dcdcdc;
  --grey-bg:#f1f1f1;
  --footer:#232323;
  --footer-text:#9a9a9a;
  --white:#ffffff;
}
*{box-sizing:border-box;margin:0;padding:0}
html,body{width:738px;height:1200px;overflow:hidden}
body{font-family:"Open Sans",Arial,sans-serif;color:var(--ink);background:var(--white);position:relative}

/* hero */
.hero{position:absolute;left:0;top:0;width:738px;height:395px;overflow:hidden}
.hero-photo{position:absolute;inset:0;background:
  linear-gradient(180deg,rgba(20,40,70,.55),rgba(30,70,120,.65)),
  linear-gradient(90deg,#4a5f78 0%,#8a9bb0 35%,#6d8098 55%,#3c5069 100%)}
.topbar{position:absolute;left:0;top:0;width:100%;height:48px;display:flex;align-items:center;padding:0 40px}
.brand{display:flex;align-items:center;gap:7px;color:var(--white);font-family:"Open Sans",sans-serif;font-weight:700;font-size:13px;letter-spacing:1px}
.brand-mark{width:22px;height:22px;background:var(--white);opacity:.9}
.nav{margin-left:auto;display:flex;gap:22px;align-items:center}
.nav a{color:var(--white);text-decoration:none;font-size:9.5px;opacity:.9;position:relative}
.nav a.active{color:#9fc4ff}
.nav a.active::before{content:"";position:absolute;left:-6px;right:-6px;top:-17px;height:2px;background:var(--blue)}
.hero-copy{position:absolute;left:0;right:0;top:222px;text-align:center;color:var(--white)}
.hero-kicker{font-family:"Josefin Sans",sans-serif;font-size:13px;font-weight:300}
.hero-title{font-family:"Josefin Sans",sans-serif;font-weight:400;font-size:29px;margin-top:4px;letter-spacing:.5px}
.hero-text{font-size:9.5px;line-height:15px;width:330px;margin:8px auto 0;opacity:.9}
.hero-actions{margin-top:20px;display:flex;justify-content:center;gap:12px}
.btn{display:inline-block;height:24px;line-height:24px;padding:0 16px;font-size:8px;font-weight:700;color:var(--white);text-decoration:none;border-radius:2px;letter-spacing:.3px}
.btn-solid{background:var(--blue)}
.btn-dark{background:rgba(15,40,80,.85)}

/* about */
.about{position:absolute;left:0;top:395px;width:738px;height:340px;padding:45px 45px 0}
.eyebrow{font-family:"Raleway",sans-serif;font-size:12px;color:#555}
.section-title{font-family:"Raleway",sans-serif;font-size:25px;font-weight:400;color:var(--ink)}
.story{position:absolute;left:45px;top:45px;width:265px}
.story .section-title{padding-bottom:8px;border-bottom:1px solid var(--line);margin-bottom:10px}
.story p{font-size:8.5px;line-height:14px;color:var(--muted)}
.more{display:block;margin-top:14px;font-size:7.5px;font-weight:700;color:var(--ink);text-decoration:none}
.proposal{position:absolute;left:375px;top:48px;width:318px;height:215px;border:1px solid var(--line);padding:0 15px}
.proposal h3{text-align:center;font-family:"Raleway",sans-serif;font-weight:400;font-size:13px;color:#555;padding:12px 0 10px;border-bottom:1px solid var(--line);margin:0 -15px 12px}
.proposal h3 strong{font-weight:600;color:var(--ink)}
.row{display:flex;gap:10px;margin-bottom:9px}
.field{flex:1;height:22px;border:1px solid var(--line);font-size:8px;color:#aaa;padding:5px 7px}
.field.message{height:48px}
.submit{display:flex;align-items:center;justify-content:space-between;height:24px;background:var(--blue);color:var(--white);font-size:8.5px;font-weight:700;padding:0 10px;margin-top:9px}
.submit-dot{width:12px;height:12px;border-radius:50%;background:var(--white);display:flex;align-items:center;justify-content:center}

/* projects */
.projects{position:absolute;left:0;top:735px;width:738px;height:330px;background:var(--grey-bg);text-align:center;padding-top:30px}
.projects .section-title{margin-top:2px}
.cards{display:flex;gap:20px;justify-content:center;margin-top:22px;text-align:left}
.card{width:210px}
.card-photo{height:140px}
.p1{background:linear-gradient(160deg,#6fa4d8,#c7d7e6 55%,#3d5a72)}
.p2{background:linear-gradient(160deg,#2c4f7a,#8eb2d6 50%,#1d3350)}
.p3{background:linear-gradient(160deg,#7fb1e0,#e3ecf4 55%,#5b86b1)}
.card h4{font-size:10px;font-weight:600;margin-top:12px}
.card p{font-size:8px;line-height:12px;color:var(--muted);margin-top:4px}
.card .more{margin-top:8px;font-size:7px}

/* footer */
.footer{position:absolute;left:0;top:1065px;width:738px;height:135px;background:var(--footer);color:var(--footer-text);display:flex;padding:22px 40px 0;gap:0}
.col h5{color:var(--white);font-size:9.5px;font-weight:600;margin-bottom:7px}
.col p,.col li{font-size:7.5px;line-height:11.5px;list-style:none}
.c1{width:185px}.c2{width:95px}.c3{width:135px}.c4{margin-left:auto;width:150px}
.c3 ul{columns:2;column-gap:10px}
.social{display:flex;gap:6px;margin-bottom:12px}
.social span{width:18px;height:18px;border:1px solid #777;border-radius:50%}
.copy{font-size:6.5px;line-height:10px}
</style>
</head>
<body>

<header class="hero">
  <div class="hero-photo" role="img" aria-label="City skyline of tall office towers under a blue tint"></div>
  <div class="topbar">
    <div class="brand"><span class="brand-mark"></span>HALVERY BUILDING GROUP</div>
    <nav class="nav">
      <a href="#" class="active">Home</a><a href="#">About</a><a href="#">Services</a><a href="#">Projects</a><a href="#">Testimonials</a><a href="#">Blog</a>
      <a href="#" aria-label="Search"><svg width="10" height="10" viewBox="0 0 10 10"><circle cx="4" cy="4" r="3" fill="none" stroke="#fff" stroke-width="1.3"/><line x1="6.2" y1="6.2" x2="9.2" y2="9.2" stroke="#fff" stroke-width="1.3"/></svg></a>
    </nav>
  </div>
  <div class="hero-copy">
    <div class="hero-kicker">Welcome to</div>
    <h1 class="hero-title">Halvery Building Group</h1>
    <p class="hero-text">Lorem Ipsum is simply dummy text of the printing and typesetting industry. Lorem Ipsum has been the industry's standard dummy text ever since the 1500s.</p>
    <div class="hero-actions"><a class="btn btn-solid" href="#">READ MORE</a><a class="btn btn-dark" href="#">GET STARTED</a></div>
  </div>
</header>

<section class="about">
  <div class="story">
    <div class="eyebrow">All About Us</div>
    <h2 class="section-title">Our Story</h2>
    <p>Lorem Ipsum is simply dummy text of the printing and typesetting industry. Lorem Ipsum has been the industry's standard dummy text ever since the 1500s, when an unknown printer took a galley of type and scrambled it to make a type specimen book. It has survived not only five centuries, but also the leap into electronic typesetting, remaining essentially unchanged. Lorem when an unknown printer took a galley of type and scrambled it to make a type specimen book.</p>
    <a class="more" href="#">READ MORE ABOUT OUR COMPANY HERE &rsaquo;</a>
  </div>
  <form class="proposal">
    <h3>Request For <strong>Proposal</strong></h3>
    <div class="row"><div class="field">Name</div><div class="field">Email</div></div>
    <div class="row"><div class="field">Subject</div><div class="field">Phone</div></div>
    <div class="field message">Message</div>
    <div class="submit">SUBMIT INQUIRY<span class="submit-dot"><svg width="6" height="6" viewBox="0 0 6 6"><path d="M2 1l2 2-2 2" fill="none" stroke="#1f63b3" stroke-width="1.2"/></svg></span></div>
  </form>
</section>

<section class="projects">
  <div class="eyebrow">Awesome Works</div>
  <h2 class="section-title">Latest Project</h2>
  <div class="cards">
    <article class="card"><div class="card-photo p1" role="img" aria-label="Modern white house with glass walls at dusk"></div><h4>Project Name</h4><p>Lorem Ipsum is simply dummy text of the printing standard dummy text ever since the 1500s</p><a class="more" href="#">READ MORE &rsaquo;</a></article>
    <article class="card"><div class="card-photo p2" role="img" aria-label="Glass office building seen from below"></div><h4>Project Name</h4><p>Lorem Ipsum is simply dummy text of the printing standard dummy text ever since the 1500s</p><a class="more" href="#">READ MORE &rsaquo;</a></article>
    <article class="card"><div class="card-photo p3" role="img" aria-label="Curved contemporary building facade"></div><h4>Project Name</h4><p>Lorem Ipsum is simply dummy text of the printing standard dummy text ever since the 1500s</p><a class="more" href="#">READ MORE &rsaquo;</a></article>
  </div>
</section>

<footer class="footer">
  <div class="col c1"><h5>Contact Us</h5><p>218 Larkmoor Street,<br>Ashford Hills, OH 44120</p><p style="margin-top:8px">Tel: 555-014-2290<br>info@halverybuildinggroup.example<br>www.halverybuildinggroup.example</p></div>
  <div class="col c2"><h5>Projects</h5><ul><li>Commercial</li><li>Residential</li><li>Community</li><li>Location Map</li></ul></div>
  <div class="col c3"><h5>Navigation</h5><ul><li>Home</li><li>About</li><li>Services</li><li>Projects</li><li>Testimonials</li><li>Blog</li><li>Contact</li></ul></div>
  <div class="col c4"><h5>Stay Connected</h5><div class="social"><span></span><span></span><span title="Workcircle"></span><span></span></div><p class="copy">&copy; 2024 Halvery Building Group.<br>All rights reserved.</p></div>
</footer>

</body>
</html>
```